Super Greens Label for Supplement Bottle

We want to design a front label for a health supplement bottle. The product is called Meadow Twist Chews™. This will be a new product so there is no current website for the product. The focus is on supergreens that taste great and deliver support for energy, digestion, and immune defense.
We want it to be modern, vibrant and appealing.
Bottle size: standard size supplement CLEAR bottle size, with white child resistant cap and the label panel dimensions are 3” x 7”. The label should be primarily white and green, with a touch of red; (see color palettes)/it can also ONLY be white and green. See samples attached.
We are only focused on the front of the bottle design, not on the back, but leave space for the supplement panel and other text on the back.
So the text for the front of the bottle is:
RT Balden's
Meadow Twist Chews™
Super Greens Blend for:
Energy, Digestion, and Immune Support*
60 Gummies | Dietary Supplement
Raspberry Flavor Gummies
Off to side of the label:
Non-GMO
Vegan Friendly
Plant-Based
Gelatin Free
Colors
Designer to choose colors to be used in the design.

```html
<!DOCTYPE html>
<html lang="en">
<head>
<meta charset="utf-8">
<title>Meadow Twist Chews – Front Label</title>
<link href="https://fonts.googleapis.com/css2?family=Montserrat:wght@300;400;600;700;800&family=Oswald:wght@300&display=swap" rel="stylesheet">
<style>
  :root {
    --bg: #eef0ee;
    --paper: #ffffff;
    --olive: #4c5d0c;
    --olive-deep: #3c4a08;
    --lime: #8db61a;
    --lime-soft: #e6f0c4;
    --red: #d0252c;
    --red-soft: #f3d3d5;
    --ink: #3e4a10;
  }
  * { margin: 0; padding: 0; box-sizing: border-box; }
  html, body { width: 1200px; height: 934px; overflow: hidden; }
  body {
    background: var(--bg);
    font-family: "Montserrat", sans-serif;
    position: relative;
  }
  .label {
    position: absolute;
    left: 238px; top: 52px;
    width: 723px; height: 830px;
    background: var(--paper);
    overflow: hidden;
    box-shadow: 0 6px 24px rgba(0,0,0,.08);
  }
  .top-band {
    position: absolute; left: 0; top: 0; width: 100%; height: 23px;
    background: var(--olive);
  }
  .bottom-band {
    position: absolute; left: 0; bottom: 0; width: 100%; height: 28px;
    background: var(--red);
  }
  .pattern-left {
    position: absolute; left: 0; top: 23px; width: 63px; height: 779px;
    background: linear-gradient(160deg, var(--lime-soft), #ffffff 80%);
  }
  .pattern-main {
    position: absolute; left: 142px; top: 23px; width: 581px; height: 779px;
    background:
      radial-gradient(ellipse 70% 45% at 95% 90%, var(--red-soft), transparent 70%),
      radial-gradient(ellipse 60% 50% at 20% 25%, #f3f7e4, transparent 70%);
    opacity: .7;
  }
  .claims-strip {
    position: absolute; left: 63px; top: 0; width: 79px; height: 583px;
    background: var(--olive);
    border-radius: 0 0 40px 40px;
    display: flex; flex-direction: column; align-items: center;
    padding-top: 102px; gap: 44px;
  }
  .claim { display: flex; flex-direction: column; align-items: center; gap: 8px; }
  .claim svg { width: 42px; height: 42px; }
  .claim span {
    font-family: "Oswald", sans-serif; font-weight: 300;
    color: #fff; font-size: 11px; line-height: 1.05; text-align: center;
    text-transform: uppercase; letter-spacing: .2px;
  }
  .count-tab {
    position: absolute; left: 63px; top: 633px; width: 79px; height: 180px;
    background: var(--red); border-radius: 40px 40px 0 0;
    color: #fff; text-align: center; padding-top: 50px;
  }
  .count-tab .num { font-size: 38px; font-weight: 400; line-height: 1; }
  .count-tab .unit { font-size: 13px; font-weight: 400; line-height: 1; margin-top: 5px; }
  .count-tab .kind { font-size: 13px; font-weight: 700; line-height: 1; }
  .count-tab .sub { font-size: 8px; font-weight: 700; line-height: 1.2; }
  .title-block {
    position: absolute; left: 142px; top: 213px; width: 581px; text-align: center;
  }
  .brand { color: var(--lime); font-weight: 600; font-size: 38px; letter-spacing: .5px; }
  .product {
    color: var(--olive-deep); font-weight: 800; font-size: 52px; line-height: 1.05;
    margin-top: 8px; letter-spacing: .5px;
  }
  .product .tm { font-size: 24px; vertical-align: super; }
  .product-line2 { color: var(--lime); font-weight: 700; font-size: 58px; line-height: 1.1; }
  .benefits-intro {
    position: absolute; left: 142px; top: 518px; width: 581px; text-align: center;
    color: var(--ink); font-weight: 300; font-size: 27px; text-transform: uppercase;
  }
  .benefits {
    position: absolute; left: 142px; top: 566px; width: 581px;
    display: flex; justify-content: center; gap: 40px;
    color: var(--olive); font-weight: 800; font-size: 19px; text-transform: uppercase;
  }
  .flavor {
    position: absolute; left: 259px; top: 730px; width: 340px; height: 34px;
    background: var(--lime); border-radius: 17px;
    display: flex; align-items: center; justify-content: center;
    color: var(--olive-deep); font-weight: 500; font-size: 18px;
  }
</style>
</head>
<body>
  <div class="label">
    <div class="pattern-left" role="img" aria-label="Fine lime diagonal line pattern"></div>
    <div class="pattern-main" role="img" aria-label="Soft flowing line waves in pale green and pink"></div>
    <div class="top-band"></div>

    <div class="claims-strip">
      <div class="claim">
        <svg viewBox="0 0 42 42" fill="none" stroke="#fff" stroke-width="1.6">
          <circle cx="21" cy="21" r="19"/>
          <path d="M13 30 L15 15 Q21 11 27 15 L29 30 Z"/>
        </svg>
        <span>Gelatin<br>Free</span>
      </div>
      <div class="claim">
        <svg viewBox="0 0 42 42" fill="none" stroke="#fff" stroke-width="1.6">
          <circle cx="21" cy="21" r="19"/>
          <path d="M12 22 H30 Q29 30 21 30 Q13 30 12 22 Z"/>
          <path d="M21 22 V14 M21 17 Q16 12 15 16 Q18 19 21 17 M21 15 Q26 10 28 13 Q25 17 21 15"/>
        </svg>
        <span>Plant<br>Based</span>
      </div>
      <div class="claim">
        <svg viewBox="0 0 42 42" fill="none" stroke="#fff" stroke-width="1.6">
          <circle cx="21" cy="21" r="19"/>
          <path d="M21 31 V20 M21 22 Q13 21 13 13 Q21 13 21 22 M21 24 Q29 23 29 15 Q21 15 21 24"/>
        </svg>
        <span>Vegan<br>Friendly</span>
      </div>
      <div class="claim">
        <svg viewBox="0 0 42 42" fill="none" stroke="#fff" stroke-width="1.6">
          <circle cx="21" cy="21" r="19"/>
          <path d="M14 30 Q21 21 28 12 M14 12 Q21 21 28 30 M16 15 H26 M15 27 H27 M18 18 H24 M18 24 H24"/>
          <path d="M8 34 L34 8"/>
        </svg>
        <span>Non<br>GMO</span>
      </div>
    </div>

    <div class="title-block">
      <div class="brand">RT Balden's</div>
      <div class="product">MEADOW TWIST</div>
      <div class="product-line2">CHEWS<span class="tm" style="font-size:24px;vertical-align:super;">™</span></div>
    </div>

    <div class="benefits-intro">Super Greens Blend For:</div>
    <div class="benefits">
      <span>Energy</span>
      <span>Digestion</span>
      <span>Immune Support*</span>
    </div>

    <div class="flavor">Raspberry Flavor Gummies</div>

    <div class="bottom-band"></div>
    <div class="count-tab">
      <div class="num">60</div>
      <div class="unit">GUMMIES</div>
      <div class="kind">DIETARY</div>
      <div class="sub">SUPPLEMENT</div>
    </div>
  </div>
</body>
</html>
```